Leaf Harbor Business Card Design

My E-Commerce store is called Leaf Harbor

Website address is - http://www.leafharbor.com.au

I would like a colourful, friendly business with the description in the 'must haves' box incorporated into it
Updates

Please add the following to the business cards; Natural & Organic Products Online Organic Pantry Items Superfoods & Supplements Natural Skincare Eco Friendly Household Products

Industry/Entity Type

Business

Contact Information for Business Card

www.leafharbor.com.au
tessa@leafharbor.com.au

Colors
acd037
9bcb3c
cadf82
eaf2ce

Requirements
Must have
• Natural & Organic Eco Products Online.
• Leaf Harbor specialises in organic pantry items, superfoods and supplements, organic skincare for you and your family & eco friendly household products.

```html
<!DOCTYPE html>
<html lang="en">
<head>
<meta charset="utf-8">
<title>Leaf Harbor Business Card</title>
<link rel="stylesheet" href="https://fonts.googleapis.com/css2?family=Didact+Gothic&family=PT+Sans:wght@400;700&display=swap">
<style>
  :root {
    --page-bg: #ece8e1;
    --card-black: #050505;
    --green-deep: #1ea64a;
    --green-brand: #2cb24f;
    --green-mid: #5cc36b;
    --green-soft: #8fd48a;
    --green-pale: #bfe5ad;
    --name-green: #c7e8a8;
    --contact-white: #f2f2f2;
    --address-ink: #36573a;
    --url-ink: #4a4d4a;
    --tagline-ink: #1f6b33;
    --divider: #6b6b6b;
  }
  * { margin: 0; padding: 0; box-sizing: border-box; }
  html, body {
    width: 1200px; height: 1146px; overflow: hidden;
    background: var(--page-bg);
  }
  .canvas { position: relative; width: 1200px; height: 1146px; }

  .card {
    position: absolute; width: 862px; height: 492px;
    border-radius: 40px; overflow: hidden;
  }
  .card--front { left: 63px; top: 49px; background: linear-gradient(100deg, var(--green-soft), var(--green-mid)); }
  .card--back {
    left: 292px; top: 590px;
    background: radial-gradient(ellipse 62% 70% at 49% 42%, var(--green-pale) 0%, var(--green-soft) 45%, var(--green-deep) 100%);
  }
  .card__shape { position: absolute; inset: 0; }

  .brand {
    position: absolute; display: flex; align-items: center; gap: 14px;
    font-family: "Didact Gothic", sans-serif; color: var(--green-brand);
    white-space: nowrap;
  }
  .brand__dot { border-radius: 50%; background: var(--green-brand); flex: none; }
  .card--front .brand { left: 92px; top: 136px; font-size: 46px; }
  .card--front .brand__dot { width: 24px; height: 24px; }
  .card--back .brand { left: 0; right: 0; top: 150px; justify-content: center; font-size: 62px; }
  .card--back .brand__dot { width: 30px; height: 30px; }

  .divider { position: absolute; left: 454px; top: 76px; width: 2px; height: 220px; background: var(--divider); }

  .person { position: absolute; left: 499px; top: 78px; font-family: "PT Sans", sans-serif; }
  .person__name { font-size: 29px; font-weight: 700; color: var(--name-green); line-height: 36px; }
  .person__title { font-size: 22px; color: var(--green-mid); letter-spacing: 1px; line-height: 30px; }

  .contacts { position: absolute; left: 499px; top: 186px; list-style: none; font-family: "PT Sans", sans-serif; }
  .contacts__item {
    display: flex; align-items: center; gap: 10px; height: 34px;
    font-size: 20px; color: var(--contact-white);
  }
  .contacts__icon { width: 16px; height: 16px; flex: none; }

  .address {
    position: absolute; right: 67px; top: 402px; text-align: right;
    font-family: "PT Sans", sans-serif; font-size: 20px; line-height: 30px;
    color: var(--address-ink); font-style: normal;
  }

  .tagline {
    position: absolute; left: 80px; right: 80px; top: 262px; text-align: center;
    font-family: "PT Sans", sans-serif; color: var(--tagline-ink);
  }
  .tagline__lead { font-size: 22px; font-weight: 700; line-height: 30px; }
  .tagline__range { font-size: 17px; line-height: 25px; margin-top: 6px; }

  .back-url {
    position: absolute; left: 0; right: 0; top: 414px; text-align: center;
    font-family: "PT Sans", sans-serif; font-size: 24px; letter-spacing: 5px;
    color: var(--url-ink);
  }
</style>
</head>
<body>
<main class="canvas">

  <section class="card card--front" aria-label="Business card front">
    <svg class="card__shape" viewBox="0 0 862 492" aria-hidden="true">
      <path fill="var(--card-black)" d="M0,0 H862 V305 C700,300 560,340 420,400 C300,450 170,440 90,410 C50,395 20,370 0,320 Z"/>
      <path fill="var(--card-black)" d="M45,425 C180,490 360,455 500,395 C620,345 740,310 855,312 C740,320 620,362 500,412 C360,472 180,505 45,425 Z"/>
    </svg>

    <div class="brand"><span class="brand__dot"></span><span class="brand__name">Leaf Harbor</span></div>

    <div class="divider"></div>

    <div class="person">
      <p class="person__name">Your Name</p>
      <p class="person__title">Title</p>
    </div>

    <ul class="contacts">
      <li class="contacts__item">
        <svg class="contacts__icon" viewBox="0 0 16 16" aria-hidden="true"><path fill="var(--green-mid)" d="M4 1.5l2.5 3-1.5 1.8c.8 1.8 2.2 3.2 4 4l1.8-1.5 3 2.5-1.6 2.5C7 13.5 2.5 9 1.5 3.1z"/></svg>
        <span>012-345-6789</span>
      </li>
      <li class="contacts__item">
        <svg class="contacts__icon" viewBox="0 0 16 16" aria-hidden="true"><rect x="1" y="4" width="14" height="9" rx="1" fill="var(--green-mid)"/><path d="M1.5 4.5L8 9.5l6.5-5" fill="none" stroke="var(--card-black)" stroke-width="1.3"/></svg>
        <span>tessa@leafharbor.com.au</span>
      </li>
      <li class="contacts__item">
        <svg class="contacts__icon" viewBox="0 0 16 16" aria-hidden="true"><g fill="none" stroke="var(--green-mid)" stroke-width="1.3"><circle cx="8" cy="8" r="6.5"/><ellipse cx="8" cy="8" rx="3" ry="6.5"/><path d="M1.5 8h13M2.5 4.8h11M2.5 11.2h11"/></g></svg>
        <span>www.leafharbor.com.au</span>
      </li>
    </ul>

    <address class="address">Street Name, City Name<br>Zipcode-012345</address>
  </section>

  <section class="card card--back" aria-label="Business card back">
    <div class="brand"><span class="brand__dot"></span><span class="brand__name">Leaf Harbor</span></div>
    <div class="tagline">
      <p class="tagline__lead">Natural &amp; Organic Eco Products Online</p>
      <p class="tagline__range">Organic Pantry Items · Superfoods &amp; Supplements<br>Natural Skincare · Eco Friendly Household Products</p>
    </div>
    <p class="back-url">www.leafharbor.com.au</p>
  </section>

</main>
</body>
</html>
```